Logo, Web and Mobile Designs for enterprise social media platform

All the details are in the attached document, please start reading the scope document first which explains what is this project about and the details about the needed deliverables, after that please read the UI_Requirements document which will detail what is expected regarding the coded web version since this is a coded contest, it is very important that you meet the UI requirements or suggest something else but we will need to agree first before working on the coded version

Good Luck

Target Market(s)

Enterprise Social Media

Industry/Entity Type

Media

Coding

Coded - Design and coding required

Number of Pages Required

5+ page

Font styles to use
Sans Serif

Requirements
Must have
• All the must haves are listed in the scope document so please check before you start

```html
<!DOCTYPE html>
<html lang="en">
<head>
<meta charset="utf-8">
<title>Staffora sign up</title>
<link href="https://fonts.googleapis.com/css2?family=Roboto:wght@300;400;500&display=swap" rel="stylesheet">
<style>
:root{
  --brand:#64b5f6;
  --brand-soft:#bbdefb;
  --brand-mid:#90caf9;
  --ink:#1f1f1f;
  --muted:#9e9e9e;
  --line:#cfcfcf;
  --panel-active:#eeeae7;
  --panel:#f5f3f2;
  --panel-faint:#f9f8f8;
  --field:#ffffff;
  --white:#ffffff;
  --alert:#f44336;
}
*{box-sizing:border-box;margin:0;padding:0}
html,body{width:1200px;height:750px;overflow:hidden;background:var(--white);font-family:'Roboto',sans-serif}
.canvas{position:relative;width:1200px;height:750px}
.topbar{position:absolute;left:0;top:0;width:1200px;height:83px;background:var(--brand);box-shadow:0 2px 3px rgba(0,0,0,.18);text-align:center}
.topbar h1{font-weight:400;font-size:50px;line-height:83px;color:var(--white);letter-spacing:.5px}
.topbar h1 .sub{color:var(--brand-soft)}
.stepper{position:absolute;left:42px;top:124px;width:1116px;height:20px;display:flex;align-items:center}
.step{display:flex;align-items:center;font-size:15px;color:var(--muted);white-space:nowrap}
.step .num{width:19px;height:19px;border-radius:50%;background:#bdbdbd;color:var(--white);font-size:12px;display:flex;align-items:center;justify-content:center;margin-right:6px}
.step.active{color:var(--ink);font-weight:500}
.step.active .num{background:var(--brand);font-weight:400}
.step-line{flex:1;height:1px;background:var(--line);margin:0 8px}
.panel{position:absolute;top:186px;height:523px}
.panel-personal{left:42px;width:336px;background:var(--panel-active);box-shadow:0 1px 3px rgba(0,0,0,.15)}
.panel-company{left:432px;width:334px;background:var(--panel)}
.panel-finish{left:820px;width:338px;background:var(--panel-faint)}
.panel-title{position:absolute;inset:0;display:flex;align-items:center;justify-content:center;text-align:center;font-weight:300;font-size:39px;line-height:35px}
.panel-company .panel-title{color:var(--brand-mid)}
.panel-finish .panel-title{color:var(--brand-soft)}
.row{position:absolute;left:0;width:336px;height:29px}
.row label,.row .label{position:absolute;right:192px;top:0;line-height:29px;font-size:14px;color:var(--muted);white-space:nowrap}
.row.focus .label{color:var(--ink)}
.field{position:absolute;left:168px;top:0;width:141px;height:29px;background:var(--field);font-size:10.5px;color:var(--muted);line-height:29px;padding-left:8px}
.row.focus .field{border:1px solid var(--brand);color:var(--ink);line-height:27px;padding-left:7px}
.pw-dots{font-size:14px;letter-spacing:1px;font-weight:500}
.date{position:absolute;top:0;height:29px;background:var(--field);font-size:10.5px;color:var(--muted);line-height:29px;padding-left:6px}
.gender{position:absolute;left:168px;top:0;height:29px;display:flex;align-items:center;font-size:11px}
.radio{width:10px;height:10px;border-radius:50%;background:var(--white);margin-right:5px;position:relative}
.radio.on::after{content:"";position:absolute;left:2px;top:2px;width:6px;height:6px;border-radius:50%;background:var(--brand)}
.gender .opt{display:flex;align-items:center;margin-right:9px}
.gender .opt.on{color:var(--ink)}
.gender .opt.off{color:#c4c4c4}
.phone-field{display:flex;align-items:center;padding-left:5px}
.phone-field svg{margin-right:4px}
.phone-field .digits{margin-left:8px}
.note{position:absolute;left:172px;top:359px;width:140px;font-size:10px;line-height:12.5px;color:#aaa}
.note .star{color:var(--alert)}
.next-bar{position:absolute;left:0;bottom:0;width:336px;height:81px;background:var(--brand);display:flex;align-items:center;justify-content:flex-end;padding-right:22px;color:var(--white);font-weight:300;font-size:39px}
.next-bar svg{margin-left:8px}
</style>
</head>
<body>
<div class="canvas">
  <header class="topbar"><h1>STAFFORA <span class="sub">sign up</span></h1></header>

  <nav class="stepper">
    <div class="step active"><span class="num">1</span>Personal info</div>
    <div class="step-line"></div>
    <div class="step"><span class="num">2</span>Company info</div>
    <div class="step-line"></div>
    <div class="step"><span class="num">3</span>Finish</div>
  </nav>

  <section class="panel panel-personal">
    <div class="row" style="top:55px"><span class="label">Name</span><div class="field">Enter your name</div></div>
    <div class="row focus" style="top:92px"><span class="label">Surname</span><div class="field">Doe</div></div>
    <div class="row" style="top:130px"><span class="label">Birthday</span>
      <div class="date" style="left:168px;width:29px">Mm</div>
      <div class="date" style="left:205px;width:29px">Dd</div>
      <div class="date" style="left:242px;width:67px">Yyyy</div>
    </div>
    <div class="row" style="top:167px"><span class="label">Gender</span>
      <div class="gender"><span class="opt on"><span class="radio on"></span>Female</span><span class="opt off"><span class="radio"></span>Male</span></div>
    </div>
    <div class="row" style="top:205px"><span class="label">E-mail</span><div class="field">Enter your e-mail</div></div>
    <div class="row" style="top:242px"><span class="label">Password</span><div class="field">Enter a password</div></div>
    <div class="row focus" style="top:279px"><span class="label">Confirm Password</span><div class="field pw-dots">••••••••</div></div>
    <div class="row" style="top:317px"><span class="label">Phone Number</span>
      <div class="field phone-field">
        <svg width="24" height="15" viewBox="0 0 24 15" aria-hidden="true">
          <rect width="24" height="15" fill="#fff"/>
          <g fill="#c62828"><rect y="0" width="24" height="1.5"/><rect y="3" width="24" height="1.5"/><rect y="6" width="24" height="1.5"/><rect y="9" width="24" height="1.5"/><rect y="12" width="24" height="1.5"/></g>
          <rect width="11" height="8" fill="#283593"/>
        </svg>
        <svg width="8" height="6" viewBox="0 0 8 6" aria-hidden="true"><path d="M1 1l3 3 3-3" fill="none" stroke="#222" stroke-width="1.4"/></svg>
        <span class="digits">000 00 0000</span>
      </div>
    </div>
    <p class="note">NOTE<span class="star">*</span> Phone number will be used to send the confirmation code</p>
    <div class="next-bar">NEXT
      <svg width="16" height="30" viewBox="0 0 16 30" aria-hidden="true"><path d="M2 2l12 13-12 13" fill="none" stroke="#fff" stroke-width="2"/></svg>
    </div>
  </section>

  <section class="panel panel-company"><div class="panel-title">COMPANY<br>INFO</div></section>
  <section class="panel panel-finish"><div class="panel-title">FINISH</div></section>
</div>
</body>
</html>
```